Nightclub-type Event Poster Advertisement

Lumora Events is based in Christchurch, New Zealand and we have our next party coming up. We like a different flair for each of our events so are looking for some help from you guys. We are very flexible with everything - colours, layout, backgrounds, fonts, etc so it's ALL up to you. Attached is our company logo and the flyer (and poster) we used for our last party. Our website is lumoranz.example where you can find and use our photos and find more info about us if you desire.
Designs we are wanting: An A3 poster,an A6 flyer (smaller version of the poster is probably fine), tickets (140x68 mm). It would be great if a 5 mm bleed was included so we could get them printed directly.
Details for the event to be advertised are as followed:
Party Name: (TBD... will update ASAP)
05/07/2014
10pm-close
Lineup: 'Bazzo (Akl)', 'DJ Glimtrax', 'DJ's Morquent & Pelnavo', 'Quiet Harbour Pulse'.
Dorrin Hattles Central, Corner Fenwick & Oberly Streets
$10 Tickets
R18
Tickets & Enquiries: Marta on 0219047362
Presented by Lumora Entertainment
Thanks to everyone who reads this and please give it a go! Any questions don't hesitate to ask.
Target Market(s)
New Zealand Europeans in Christchurch, New Zealand between 18 and 25 years old.
Industry/Entity Type
Events
Look and feel

```html
<!DOCTYPE html>
<html lang="en">
<head>
<meta charset="utf-8">
<title>The Big Party – Lumora Events</title>
<link rel="stylesheet" href="https://fonts.googleapis.com/css2?family=Josefin+Sans:wght@300;400;600;700&display=swap">
<style>
  :root {
    --page-bg: #e9e8e6;
    --poster-dark: #0b0f0d;
    --poster-mid: #1d2a1e;
    --magenta: #c0187a;
    --magenta-light: #e0349b;
    --white: #ffffff;
  }
  * { margin: 0; padding: 0; box-sizing: border-box; }
  html, body {
    width: 1200px;
    height: 1148px;
    overflow: hidden;
    background: var(--page-bg);
    font-family: "Josefin Sans", sans-serif;
  }
  .poster {
    position: absolute;
    left: 200px;
    top: 16px;
    width: 800px;
    height: 1116px;
    overflow: hidden;
    background: var(--poster-dark);
  }
  .poster__photo {
    position: absolute;
    inset: 0;
    background:
      radial-gradient(ellipse 260px 180px at 170px 1000px, rgba(110,130,60,0.55), transparent 70%),
      radial-gradient(ellipse 300px 260px at 160px 420px, rgba(92,106,42,0.45), transparent 70%),
      radial-gradient(ellipse 280px 240px at 640px 360px, rgba(70,90,50,0.35), transparent 70%),
      radial-gradient(ellipse 360px 300px at 420px 620px, rgba(47,74,68,0.35), transparent 70%),
      linear-gradient(180deg, var(--poster-mid) 0%, var(--poster-dark) 55%, #121a14 100%);
  }
  .poster__art {
    position: absolute;
    inset: 0;
    width: 800px;
    height: 1116px;
  }
  .band--deep { fill: var(--magenta); }
  .band--light { fill: var(--magenta-light); }
  .date-badge, .bolt { fill: var(--magenta); }
  .presenter {
    fill: var(--white);
    font-weight: 300;
    font-size: 26px;
  }
  .title {
    fill: var(--white);
    font-weight: 300;
  }
  .date {
    fill: var(--white);
    font-weight: 400;
    font-size: 34px;
  }
  .lineup {
    fill: var(--white);
    font-weight: 600;
  }
  .details {
    fill: var(--white);
    font-weight: 300;
    font-size: 22px;
    opacity: 0.9;
  }
</style>
</head>
<body>
  <main class="poster">
    <div class="poster__photo" role="img" aria-label="Blurred disco lights with a mirror ball in the lower left, in dark green and olive tones"></div>
    <svg class="poster__art" viewBox="0 0 800 1116" xmlns="http://www.w3.org/2000/svg">
      <g class="top-bands">
        <polygon class="band--light" points="0,70 800,0 800,10 0,80"/>
        <polygon class="band--deep" points="0,84 800,14 800,34 0,106"/>
      </g>

      <text class="presenter" x="380" y="112" text-anchor="middle">LUMORA EVENTS <tspan font-size="24">presents</tspan></text>

      <text class="title" x="177" y="251" font-size="122" textLength="167" lengthAdjust="spacingAndGlyphs">THE</text>
      <text class="title" x="84" y="381" font-size="164" textLength="586" lengthAdjust="spacingAndGlyphs">BIG PARTY</text>

      <polygon class="date-badge" points="223,440 300,391 474,391 474,400 445,456 258,456"/>
      <text class="date" x="350" y="436" text-anchor="middle">05/07/14</text>

      <g class="bolts">
        <polygon class="bolt" points="560,470 600,420 588,450 640,395 600,470 612,440"/>
        <polygon class="bolt" points="130,510 175,520 160,526 200,545 150,532 162,526"/>
        <polygon class="bolt" points="620,772 660,782 648,788 700,808 640,796 652,790"/>
      </g>

      <g class="lineup" text-anchor="middle">
        <text x="430" y="572" font-size="66">BAZZO (AKL)</text>
        <text x="430" y="634" font-size="54">DJ GLIMTRAX</text>
        <text x="430" y="692" font-size="40">DJ'S MORQUENT &amp; PELNAVO</text>
        <text x="430" y="750" font-size="46">QUIET HARBOUR PULSE</text>
      </g>

      <g class="details">
        <text x="108" y="818">$10 TICKETS · R18</text>
        <text x="108" y="850">opening 10pm – close</text>
        <text x="108" y="882">Dorrin Hattles Central</text>
        <text x="108" y="914">Corner Fenwick &amp; Oberly Streets</text>
        <text x="108" y="946">Tickets &amp; Enquiries: Marta on 0219047362</text>
        <text x="108" y="978">Presented by Lumora Entertainment</text>
      </g>

      <g class="bottom-bands">
        <polygon class="band--light" points="0,1080 800,950 800,962 0,1092"/>
        <polygon class="band--deep" points="0,1096 800,966 800,992 0,1116"/>
      </g>
    </svg>
  </main>
</body>
</html>
```